Business card for wedding & event planning company

I'm looking for a well designed double sided business card to represent my wedding and event planning company.

It should include the fact we manage the following events:
Weddings, birthdays, conferences, product launches, fashion shows & conventions
in the following areas:
Wiltshire, Oxfordshire, Berkshire & London

My contact details to be included are:

Moira Lintell
07741 308562
moira@amberfinchgatherings.co.uk
www.amberfinchgatherings.co.uk

My logo can be found at the following Filevaultly location:
AI file: https://www.filevaultly.com/s/k3mprt8wq51bn2x/brief_480317_2290451_7735102_sourcefile.ai?dl=0
PNG file:
https://www.filevaultly.com/s/hv7ncqeyb4tlofu/brief_480317_2290451_7735102_e8a1b406_image.png?dl=0

Target Market(s)

women aged 30-55

Industry/Entity Type

Wedding

Contact Information for Business Card

in the following areas:

Moira Lintell
Event Planner
07741 308562

Font styles to use
Serif
Sans Serif
Script

Requirements
Must have
• Purple and white colour scheme
Should not have
• Black background
• Please don't submit any of the see-through business card designs.

```html
<!DOCTYPE html>
<html lang="en">
<head>
<meta charset="utf-8">
<title>Amber Finch Gatherings – Business Card</title>
<link rel="stylesheet" href="https://fonts.googleapis.com/css2?family=Great+Vibes&family=Tinos&display=swap">
<style>
  :root {
    --purple: #8a2f8e;
    --purple-soft: #c9a6cc;
    --ribbon: #ece3ee;
    --white: #ffffff;
    --backdrop: #b7b1b3;
    --shadow: rgba(0,0,0,0.28);
  }
  * { box-sizing: border-box; margin: 0; padding: 0; }
  html, body { width: 1200px; height: 1000px; overflow: hidden; }
  body { background: var(--backdrop); position: relative; font-family: "Tinos", "Times New Roman", serif; }

  .card {
    position: absolute;
    width: 690px;
    height: 415px;
    box-shadow: 0 6px 14px var(--shadow);
    overflow: hidden;
  }
  .card--front { left: 70px; top: 85px; background: var(--white); color: var(--purple); }
  .card--back { left: 430px; top: 545px; background: var(--purple); color: var(--white); }

  .ribbon-pattern {
    position: absolute;
    right: 0; top: 0;
    width: 330px; height: 415px;
    background: radial-gradient(ellipse at 60% 55%, var(--ribbon) 0%, rgba(236,227,238,0.5) 45%, rgba(255,255,255,0) 75%);
  }

  .brand {
    position: absolute;
    text-align: center;
    font-family: "Tinos", "Times New Roman", serif;
    font-weight: 400;
    letter-spacing: 1px;
  }
  .brand__mark {
    display: block;
    width: 78px; height: 78px;
    margin: 0 auto 10px;
    border: 2px solid currentColor;
    border-radius: 50%;
  }
  .brand__name { display: block; font-size: 34px; line-height: 1; text-transform: uppercase; }
  .brand__sub { display: block; font-size: 14px; letter-spacing: 3px; margin-top: 6px; text-transform: uppercase; }
  .card--front .brand { left: 380px; top: 30px; width: 280px; }
  .card--back .brand { left: 200px; top: 40px; width: 300px; }

  .contact-name {
    position: absolute; left: 52px; top: 200px;
    font-family: "Great Vibes", cursive;
    font-size: 36px;
  }
  .contact-list { position: absolute; left: 52px; top: 262px; list-style: none; }
  .contact-list li { display: flex; align-items: center; gap: 12px; height: 36px; font-size: 19px; }
  .contact-list li.web { font-size: 16px; }
  .icon { width: 26px; height: 26px; flex: none; }

  .services {
    position: absolute; left: 40px; right: 40px; top: 192px;
    text-align: center; font-size: 19px; line-height: 1.2;
  }
  .areas { position: absolute; left: 290px; top: 262px; list-style: none; font-size: 19px; }
  .areas li { display: flex; align-items: center; gap: 8px; height: 24px; }
  .pin { width: 10px; height: 14px; }

  .faint-circle {
    position: absolute; left: 430px; top: 150px;
    width: 230px; height: 230px;
    border: 3px solid var(--purple-soft);
    border-radius: 50%;
    opacity: 0.45;
  }
</style>
</head>
<body>

<section class="card card--front" aria-label="Business card front">
  <div class="ribbon-pattern" role="img" aria-label="Soft lilac looping ribbon pattern"></div>

  <div class="brand">
    <span class="brand__mark"></span>
    <span class="brand__name">Amber Finch</span>
    <span class="brand__sub">Gatherings</span>
  </div>

  <p class="contact-name">Moira Lintell</p>

  <ul class="contact-list">
    <li>
      <svg class="icon" viewBox="0 0 26 26" aria-hidden="true">
        <circle cx="13" cy="13" r="12" fill="none" stroke="currentColor" stroke-width="2"/>
        <path d="M9 7.5c-1.5 1-1.5 3 0 5.5s3.5 4.5 5.8 5.5c1.5.5 2.6 0 3.2-1l-2.3-2-1.3.8c-1.2-.6-2.5-2-3.1-3.2l.8-1.3-2-2.3z" fill="currentColor"/>
      </svg>
      <span>07741 308562</span>
    </li>
    <li>
      <svg class="icon" viewBox="0 0 26 26" aria-hidden="true">
        <circle cx="13" cy="13" r="12.5" fill="currentColor"/>
        <rect x="6.5" y="8.5" width="13" height="9" fill="none" stroke="#fff" stroke-width="1.4"/>
        <path d="M6.5 8.5l6.5 5 6.5-5" fill="none" stroke="#fff" stroke-width="1.4"/>
      </svg>
      <span>moira@amberfinchgatherings.co.uk</span>
    </li>
    <li class="web">
      <svg class="icon" viewBox="0 0 26 26" aria-hidden="true">
        <circle cx="13" cy="13" r="12.5" fill="currentColor"/>
        <g fill="none" stroke="#fff" stroke-width="1.2">
          <circle cx="13" cy="13" r="7"/>
          <ellipse cx="13" cy="13" rx="3" ry="7"/>
          <path d="M6 13h14M7 9.5h12M7 16.5h12"/>
        </g>
      </svg>
      <span>www.amberfinchgatherings.co.uk</span>
    </li>
  </ul>
</section>

<section class="card card--back" aria-label="Business card back">
  <span class="faint-circle"></span>

  <div class="brand">
    <span class="brand__mark"></span>
    <span class="brand__name">Amber Finch</span>
    <span class="brand__sub">Gatherings</span>
  </div>

  <p class="services">Weddings, birthdays, conferences, product launches, fashion shows<br>&amp; conventions in the following areas :</p>

  <ul class="areas">
    <li><svg class="pin" viewBox="0 0 10 14" aria-hidden="true"><path d="M5 0a5 5 0 0 1 5 5c0 3.5-5 9-5 9S0 8.5 0 5a5 5 0 0 1 5-5z" fill="#fff"/><circle cx="5" cy="5" r="1.8" fill="var(--purple)"/></svg>Wiltshire</li>
    <li><svg class="pin" viewBox="0 0 10 14" aria-hidden="true"><path d="M5 0a5 5 0 0 1 5 5c0 3.5-5 9-5 9S0 8.5 0 5a5 5 0 0 1 5-5z" fill="#fff"/><circle cx="5" cy="5" r="1.8" fill="var(--purple)"/></svg>Oxfordshire</li>
    <li><svg class="pin" viewBox="0 0 10 14" aria-hidden="true"><path d="M5 0a5 5 0 0 1 5 5c0 3.5-5 9-5 9S0 8.5 0 5a5 5 0 0 1 5-5z" fill="#fff"/><circle cx="5" cy="5" r="1.8" fill="var(--purple)"/></svg>Berkshire</li>
    <li><svg class="pin" viewBox="0 0 10 14" aria-hidden="true"><path d="M5 0a5 5 0 0 1 5 5c0 3.5-5 9-5 9S0 8.5 0 5a5 5 0 0 1 5-5z" fill="#fff"/><circle cx="5" cy="5" r="1.8" fill="var(--purple)"/></svg>London</li>
  </ul>
</section>

</body>
</html>
```